Construction business card

We are a family run and family oriented business in Philadelphia and we are starting new. We proudly serve the public by giving our customers great work at affordable prices. We can do all aspects of construction from the roof to the basement. We would like our business card to incorporate tools and family.
Updates

Can y'all please incorporate a bulldog

Industry/Entity Type

Construction

Contact Information for Business Card

Harbor Builders LLC, Dennis Whitcomb, 1187 W 9th st Philadelphia Pa 19140, CEO Main phone (215) 555-0143 cellphone 215-555-0187 Dennis whitcomb Jr cellphone 267-555-0129 email harborbuildersllc@quillpost.example

Colors
f78f20
ffffff
1b1b1b

```html
<!DOCTYPE html>
<html lang="en">
<head>
<meta charset="utf-8">
<title>Harbor Builders LLC — Business Card</title>
<link href="https://fonts.googleapis.com/css2?family=Questrial&display=swap" rel="stylesheet">
<style>
  :root {
    --orange: #f78f20;
    --white: #ffffff;
    --ink: #1b1b1b;
    --grey: #8a8a8a;
    --backdrop: #e9e7e3;
  }
  html, body {
    margin: 0;
    padding: 0;
    width: 1200px;
    height: 1184px;
    overflow: hidden;
    background: var(--backdrop);
    font-family: "Questrial", sans-serif;
  }
  .sheet {
    width: 1200px;
    height: 1184px;
    display: flex;
    flex-direction: column;
    align-items: center;
    justify-content: center;
    gap: 40px;
  }
  .card {
    position: relative;
    width: 960px;
    height: 530px;
    background: var(--white);
    box-shadow: 0 6px 18px rgba(0,0,0,0.12);
    box-sizing: border-box;
  }
  .card--front {
    display: flex;
    align-items: center;
    justify-content: center;
  }
  .wordmark {
    color: var(--orange);
    font-weight: 400;
    letter-spacing: 6px;
    line-height: 1;
  }
  .card--front .wordmark { font-size: 180px; }

  .card--back .wordmark {
    position: absolute;
    left: 90px;
    top: 80px;
    font-size: 86px;
    letter-spacing: 3px;
  }
  .company-name {
    position: absolute;
    left: 90px;
    top: 205px;
    margin: 0;
    font-size: 29px;
    font-weight: 400;
    letter-spacing: 3px;
    text-transform: uppercase;
    color: var(--ink);
  }
  .divider {
    position: absolute;
    left: 90px;
    right: 70px;
    top: 338px;
    height: 1px;
    background: var(--orange);
  }
  .person {
    position: absolute;
    left: 90px;
    top: 296px;
  }
  .person-name {
    margin: 0;
    font-size: 34px;
    font-weight: 400;
    letter-spacing: 1px;
    text-transform: uppercase;
    line-height: 1;
  }
  .person-name .first { color: var(--orange); }
  .person-name .last { color: var(--grey); }
  .person-title {
    margin: 14px 0 0;
    font-size: 18px;
    letter-spacing: 10px;
    color: var(--grey);
  }
  .contact {
    position: absolute;
    right: 70px;
    top: 360px;
    margin: 0;
    padding: 0;
    list-style: none;
    text-align: right;
  }
  .contact li {
    display: flex;
    align-items: center;
    justify-content: flex-end;
    gap: 14px;
    font-size: 18px;
    color: var(--grey);
    height: 34px;
  }
  .contact svg { width: 18px; height: 22px; flex: none; }
</style>
</head>
<body>
<main class="sheet">
  <section class="card card--front" aria-label="Card front">
    <div class="wordmark">HARBOR</div>
  </section>

  <section class="card card--back" aria-label="Card back">
    <div class="wordmark">HARBOR</div>
    <h1 class="company-name">Harbor Builders LLC</h1>
    <div class="divider"></div>
    <div class="person">
      <p class="person-name"><span class="first">Dennis</span><span class="last">Whitcomb</span></p>
      <p class="person-title">Ceo</p>
    </div>
    <ul class="contact">
      <li>
        <span>(215) 555-0143</span>
        <svg viewBox="0 0 18 22" aria-hidden="true">
          <rect x="3" y="1" width="12" height="20" rx="2" fill="var(--orange)"/>
          <rect x="5" y="4" width="8" height="10" fill="var(--white)"/>
          <circle cx="9" cy="17.5" r="1.4" fill="var(--white)"/>
        </svg>
      </li>
      <li>
        <span>1187 W 9th st Philadelphia Pa 19140</span>
        <svg viewBox="0 0 18 22" aria-hidden="true">
          <path d="M9 1C5 1 2 4 2 8c0 5 7 13 7 13s7-8 7-13c0-4-3-7-7-7z" fill="var(--orange)"/>
          <circle cx="9" cy="8" r="2.6" fill="var(--white)"/>
        </svg>
      </li>
    </ul>
  </section>
</main>
</body>
</html>
```